Banner Ad Design Project

I need a banner design. The website is under construction at www.brightmarrow.example

Name: Bright Marrow
Tagline: Steady Sparks for crowded calendars

This is a leadership development and executive coaching site. The past site is live at www.quillstepnow.example. (so you can get a sense of the content)

The audience are (BUSY) executives, senior managers, leaders and top professionals, so the feel needs to be highly professional but also modern and fresh. I want to communicate energy but also solid and trust worthy and not too new agey. The audience are also people with strong social values who want to change things - so not too corporate (Ie suits!)

I would like the design to be floating on a white background, very clean and simple. I am attracted to reds or sunset (burn orange crimson colors.) But totally open to any color ideas.
I am giving an open brief for your ideas.
Here are the dimensions 960px wide, roughly 190px height.

Reason: The weekend might give more time to designers to get involved. Thanks Vina

Hi designers

You may not have seen the additions I gave to this brief.

The banner should not have leader out front photo's. Maybe less corporate than I initially thought. 
Not too corporate (no suits!) Please no chess pieces, jigsaw pieces, cartoon images, cliche leadership images. 
Am am trying for inspiration /inspiring whilst still being professional. Very simple and clean.
Please can the design be floating in a white background so that the web page is borderless - A bit like it is in http://palmoriskel.example/
Thank you

Target Market(s)

Senior managers, executives but people who also want to change the world!

Industry/Entity Type

Construction

Requirements
Should not have
• Should not have leader out front photo's.
Maybe less corporate than I initially thought.
Am am trying for inspiration /inspiring whilst still being professional.
Please no chess pieces, jigsaw pieces, cartoon images, cliche leadership images. Not too corporate (Ie suits!)

Thanks

```html
<!DOCTYPE html>
<html lang="en">
<head>
<meta charset="utf-8">
<title>Bright Marrow banner</title>
<link rel="stylesheet" href="https://fonts.googleapis.com/css2?family=PT+Sans:wght@400&display=swap">
<style>
  :root {
    --canvas-white: #ffffff;
    --mist: #f3f3f3;
    --mist-deep: #e8e8e8;
    --ember: #d64a10;
    --glow-soft: #f6e6da;
    --glow-warm: #efcdb4;
  }
  html, body {
    margin: 0;
    padding: 0;
    width: 1200px;
    height: 238px;
    overflow: hidden;
    background: var(--canvas-white);
  }
  .banner {
    position: relative;
    width: 1200px;
    height: 238px;
    overflow: hidden;
    background:
      radial-gradient(ellipse 70% 120% at 35% 60%, var(--canvas-white) 40%, transparent 100%),
      linear-gradient(180deg, var(--mist-deep) 0%, var(--mist) 35%, var(--canvas-white) 100%);
    font-family: "PT Sans", "Myriad Pro", sans-serif;
  }
  .banner__tagline {
    position: absolute;
    left: 110px;
    top: 54px;
    margin: 0;
    font-weight: 400;
    font-size: 43px;
    line-height: 59px;
    letter-spacing: -0.2px;
    color: var(--ember);
  }
  .banner__visual {
    position: absolute;
    top: 0;
    right: 0;
    width: 440px;
    height: 238px;
    background:
      linear-gradient(90deg, var(--canvas-white) 0%, rgba(255,255,255,0) 45%),
      linear-gradient(180deg, rgba(255,255,255,0) 55%, var(--canvas-white) 100%),
      linear-gradient(160deg, var(--glow-soft) 0%, var(--glow-warm) 100%);
  }
  .banner__name {
    position: absolute;
    right: 40px;
    bottom: 28px;
    display: flex;
    align-items: center;
    gap: 10px;
    margin: 0;
    font-weight: 400;
    font-size: 24px;
    line-height: 1;
    color: var(--ember);
  }
  .banner__name-dot {
    width: 12px;
    height: 12px;
    border-radius: 50%;
    background: var(--ember);
  }
</style>
</head>
<body>
  <div class="banner">
    <h1 class="banner__tagline">Steady Sparks for<br>crowded calendars..</h1>
    <div class="banner__visual" role="img" aria-label="Soft warm sunset-toned backdrop fading into white"></div>
    <p class="banner__name"><span class="banner__name-dot"></span>Bright Marrow</p>
  </div>
</body>
</html>
```